Lantern Grove Bridal Show Flyer

I need designed a reusable flyer that is more eye catching than my current flyer. I would also need separate layers as the details change from show to show. I attached the flyer I currently use.

Wedding

```html
<!DOCTYPE html>
<html lang="en">
<head>
<meta charset="utf-8">
<title>Lantern Grove Bridal Show Flyer</title>
<link href="https://fonts.googleapis.com/css2?family=Great+Vibes&family=Roboto+Condensed:ital,wght@0,400;0,700;1,700&family=Open+Sans:ital,wght@0,300;0,400;0,600;1,300&display=swap" rel="stylesheet">
<style>
  :root {
    --page-bg: #efece8;
    --paper: #ffffff;
    --green-deep: #1c5f30;
    --green-mid: #2d8446;
    --green-text: #1f8a3c;
    --sky: #5aa4de;
    --sky-light: #a9d3f1;
    --sky-pale: #dcedfa;
    --ink: #2b2b2b;
    --white: #ffffff;
  }
  * { margin: 0; padding: 0; box-sizing: border-box; }
  html, body { width: 1200px; height: 1000px; overflow: hidden; background: var(--page-bg); }
  .flyer {
    position: absolute; left: 275px; top: 78px; width: 653px; height: 844px;
    background: var(--paper); overflow: hidden;
    font-family: "Open Sans", sans-serif; color: var(--ink);
  }
  .flyer-shapes { position: absolute; inset: 0; }
  .abs { position: absolute; }

  .title-badge { left: 30px; top: 36px; width: 375px; height: 292px; text-align: center; }
  .title-script {
    font-family: "Great Vibes", cursive; color: var(--green-text);
    font-size: 64px; line-height: 50px;
  }
  .title-script.first { position: absolute; left: 0; right: 0; top: 82px; }
  .title-script.second { position: absolute; left: 0; right: 0; top: 134px; }
  .title-sub {
    position: absolute; left: 0; right: 0; font-style: italic; font-weight: 300;
    font-size: 19px; color: #333;
  }
  .title-sub.casting { top: 194px; }
  .title-sub.dress { top: 219px; }
  .title-sub strong { color: var(--green-text); font-weight: 600; }

  .event { color: var(--white); font-family: "Roboto Condensed", sans-serif; }
  .prize { left: 40px; top: 362px; width: 340px; display: flex; align-items: center; justify-content: center; gap: 8px; }
  .prize-lead { font-size: 13px; line-height: 16px; text-align: right; text-transform: uppercase; padding-right: 8px; border-right: 1px solid var(--white); }
  .prize-amount { font-size: 32px; }
  .rule { left: 70px; top: 407px; width: 300px; border-top: 1px dotted rgba(255,255,255,0.6); }
  .date { left: 20px; width: 400px; top: 412px; text-align: center; font-size: 17px; }
  .venue { left: 20px; width: 400px; top: 435px; text-align: center; font-size: 23px; }
  .address { left: 20px; width: 400px; top: 464px; text-align: center; font-size: 15px; }
  .coupon {
    left: 97px; top: 499px; width: 241px; height: 66px;
    background: var(--sky); border: 2px dashed var(--white);
    color: var(--white); font-family: "Roboto Condensed", sans-serif; font-size: 19px;
    line-height: 23px; text-align: center; padding-top: 9px;
  }

  .brand-name { left: 33px; top: 642px; font-family: "Open Sans", sans-serif; font-size: 32px; color: var(--sky); font-weight: 400; letter-spacing: -0.5px; }
  .sponsor { left: 20px; width: 290px; top: 692px; text-align: center; font-size: 14px; line-height: 20px; }
  .sponsor .lead { color: #555; }
  .tickets { left: 50px; width: 240px; top: 742px; text-align: center; font-size: 19px; font-weight: 600; color: #333; }
  .contact-line { left: 48px; display: flex; align-items: center; gap: 14px; color: var(--green-text); font-weight: 600; }
  .contact-line.web { top: 768px; font-size: 21px; }
  .contact-line.phone { top: 796px; font-size: 27px; }
  .contact-line svg { width: 24px; height: 24px; }

  .giveaway {
    left: 325px; width: 160px; top: 680px; text-align: center;
    font-family: "Roboto Condensed", sans-serif; font-style: italic; font-weight: 700;
    font-size: 24px; line-height: 27px; color: var(--white);
  }
  .partner { left: 492px; top: 752px; width: 140px; display: flex; flex-direction: column; align-items: center; gap: 6px; }
  .partner-mark { width: 14px; height: 14px; border-radius: 50%; background: var(--sky); }
  .partner-name { font-family: "Open Sans", sans-serif; font-weight: 600; font-size: 17px; line-height: 21px; color: var(--green-text); text-align: center; }
</style>
</head>
<body>
  <main class="flyer">
    <svg class="flyer-shapes" viewBox="0 0 653 844" width="653" height="844">
      <defs>
        <linearGradient id="greenField" x1="0" y1="0" x2="1" y2="1">
          <stop offset="0" stop-color="#2e8a48"/>
          <stop offset="1" stop-color="#1a5a2d"/>
        </linearGradient>
        <linearGradient id="portraitTone" x1="0" y1="0" x2="0" y2="1">
          <stop offset="0" stop-color="#2b6e3d"/>
          <stop offset="0.45" stop-color="#c99b85"/>
          <stop offset="1" stop-color="#f3efe9"/>
        </linearGradient>
        <linearGradient id="seaTone" x1="0" y1="0" x2="0" y2="1">
          <stop offset="0" stop-color="#8cc7ec"/>
          <stop offset="0.55" stop-color="#f4f6f8"/>
          <stop offset="1" stop-color="#3b9ab7"/>
        </linearGradient>
      </defs>
      <path d="M0 0 H653 V560 Q330 640 0 567 Z" fill="url(#greenField)"/>
      <path d="M0 567 Q330 640 653 560" fill="none" stroke="var(--sky)" stroke-width="5"/>
      <rect x="420" y="20" width="225" height="520" rx="90" fill="url(#portraitTone)" role="img" aria-label="Smiling bride in a strapless white gown with a green birdcage veil fascinator"/>
      <rect x="30" y="36" width="375" height="292" rx="46" fill="var(--sky-light)"/>
      <rect x="40" y="46" width="355" height="272" rx="40" fill="var(--paper)" stroke="var(--sky)" stroke-width="3"/>
      <rect x="52" y="58" width="331" height="248" rx="34" fill="none" stroke="var(--sky-light)" stroke-width="1" stroke-dasharray="3 3"/>
      <circle cx="522" cy="590" r="124" fill="var(--sky-light)"/>
      <circle cx="522" cy="590" r="112" fill="url(#seaTone)" role="img" aria-label="White cruise ship on turquoise water"/>
      <circle cx="405" cy="717" r="92" fill="var(--sky-pale)"/>
      <circle cx="405" cy="717" r="80" fill="var(--sky)"/>
    </svg>

    <div class="abs title-badge">
      <div class="title-script first">Bridal</div>
      <div class="title-script second">Show</div>
      <div class="title-sub casting">Open Casting Call</div>
      <div class="title-sub dress">Find Your <strong>Dream</strong> Dress</div>
    </div>

    <div class="abs event prize">
      <div class="prize-lead">The first 50 brides will<br>get a chance to win</div>
      <div class="prize-amount">$25,000</div>
    </div>
    <div class="abs rule"></div>
    <div class="abs event date">Tuesday • September 16th • 6:00-9:00 PM</div>
    <div class="abs event venue">The Harbor Room at Castellano's</div>
    <div class="abs event address">1520 Shore Road, Maplewood, CT</div>
    <div class="abs coupon">$3 off admission by using<br>coupon code NP3</div>

    <div class="abs brand-name">Lantern Grove</div>
    <div class="abs sponsor"><div class="lead">Sponsored by</div><div>Moonlit Melody Entertainment</div></div>
    <div class="abs tickets">Get Tickets at</div>
    <div class="abs contact-line web">
      <svg viewBox="0 0 24 24" aria-hidden="true"><circle cx="12" cy="12" r="10" fill="none" stroke="#222" stroke-width="2"/><ellipse cx="12" cy="12" rx="4.5" ry="10" fill="none" stroke="#222" stroke-width="1.6"/><path d="M2 12H22M4 7H20M4 17H20" stroke="#222" stroke-width="1.4"/></svg>
      <span>lanterngrove.com</span>
    </div>
    <div class="abs contact-line phone">
      <svg viewBox="0 0 24 24" aria-hidden="true"><circle cx="12" cy="12" r="10.5" fill="none" stroke="#222" stroke-width="2"/><path d="M8.5 6.5l2 2.5-1.2 1.5c.8 1.7 2 2.9 3.7 3.7l1.5-1.2 2.5 2-1.3 1.8c-4.2-.6-7.6-4-8.2-8.2z" fill="#222"/></svg>
      <span>203-555-0148</span>
    </div>

    <div class="abs giveaway">HONEYMOON<br>CRUISE<br>GIVEAWAY</div>
    <div class="abs partner"><span class="partner-mark"></span><span class="partner-name">Harborlight<br>Radio</span></div>
  </main>
</body>
</html>
```